Brimwave.com fiber optic internet website redesign

We need a new website design for our fiber optic internet company that provides internet, phone, and tv services. It should use the text "Tamberlyn fiber optics", and "Shine brighter on Tamberlyn". The design should use the color blue and the attached logo.
We are a 30 year old internet company who started as a dial up internet provider in our basement. Today we design, build, and maintain our own fiber optic internet network to provide service to residential, business, educational, healthcare, and governmental customers

```html
<!DOCTYPE html>
<html lang="en">
<head>
<meta charset="utf-8">
<title>Brimwave.com — Tamberlyn Fiber Optics</title>
<link rel="stylesheet" href="https://fonts.googleapis.com/css2?family=Poppins:wght@300;400;500;600;700&family=Open+Sans:wght@400;600;700&display=swap">
<style>
:root{
  --blue:#1b4fa8;
  --nav-blue:#2b5bb8;
  --accent:#1f6fe0;
  --accent-dark:#1656b8;
  --accent-light:#5c9cf2;
  --ink:#111418;
  --hero-bg:#dcecf8;
  --band-bg:#e7f2fb;
  --dark:#2e313e;
  --contact-bg:#eef0fb;
  --form-bg:#c7c8f4;
  --foot-bar:#e8f2fb;
  --soft:#d6e6fb;
}
*{margin:0;padding:0;box-sizing:border-box}
html,body{width:1200px;height:5102px;overflow:hidden}
body{font-family:"Open Sans",Arial,sans-serif;color:var(--ink);background:#fff;position:relative}
.abs{position:absolute}
section,header,footer{position:absolute;left:0;width:1200px}
.brand{display:flex;align-items:center;gap:10px}
.brand-dot{width:58px;height:58px;border-radius:50%;background:var(--blue)}
.brand-name{font-family:"Poppins",sans-serif;font-weight:600;font-size:33px;color:var(--ink);line-height:1}
.brand-tag{font-size:12px;color:var(--ink);margin-top:2px}
/* header */
.site-header{top:0;height:88px;background:#fff}
.site-header .brand{position:absolute;left:72px;top:14px}
.nav{position:absolute;left:428px;top:28px;display:flex;gap:22px;font-size:17px;color:var(--nav-blue)}
.nav-icons{position:absolute;left:1105px;top:28px;display:flex;gap:16px}
/* hero */
.hero{top:88px;height:516px;background:linear-gradient(90deg,#e6f2fb,var(--hero-bg))}
.hero-kicker{left:80px;top:108px;font-size:21px;display:flex;align-items:center;gap:14px}
.hero-kicker:before{content:"";width:62px;height:2px;background:var(--accent)}
.hero h1{left:72px;top:148px;width:600px;font-family:"Poppins",sans-serif;font-weight:600;font-size:37px;line-height:53px}
.hero-text{left:76px;top:318px;width:600px;font-size:18px;line-height:26px}
.btn{display:flex;align-items:center;justify-content:center;font-size:18px}
.btn-accent{background:var(--accent);color:#fff}
.btn-outline{border:2px solid var(--accent);color:var(--accent);background:#fff}
.hero-art{left:690px;top:50px;width:460px;height:380px;border-radius:20px;background:radial-gradient(circle at 55% 55%,#a9a9d6 0,#cfd5ec 45%,rgba(220,236,248,0) 72%)}
.dots{left:566px;top:486px;display:flex;gap:8px}
.dots i{width:14px;height:14px;border-radius:50%;background:var(--accent)}
.dots i:first-child{background:#111}
/* services */
.services{top:604px;height:686px;background:#fff}
.eyebrow{font-family:"Poppins",sans-serif;color:var(--accent);font-weight:600;font-size:19px}
.h2{font-family:"Poppins",sans-serif;font-weight:600;font-size:38px;color:var(--ink)}
.arrows{left:1046px;top:186px;display:flex;gap:6px}
.arrows i{width:24px;height:24px;border:1px solid #dde4ee;display:flex;align-items:center;justify-content:center;color:var(--accent);font-style:normal;font-size:13px}
.card{top:246px;width:230px;height:346px;background:#fff;border-top:6px solid var(--accent);box-shadow:0 4px 14px rgba(0,0,0,.14);text-align:center;padding-top:30px}
.card h3{font-family:"Poppins",sans-serif;font-weight:500;font-size:20px;margin:18px 0 12px}
.card p{font-size:14px;line-height:26px;width:190px;margin:0 auto}
.card a{display:block;margin-top:16px;color:var(--accent);font-weight:700;font-size:18px;text-decoration:none}
/* residential */
.residential{top:1290px;height:680px;background:var(--band-bg)}
.photo-circle{border-radius:50%}
.res-title{font-family:"Poppins",sans-serif;font-weight:600;font-size:39px;line-height:52px}
.g{color:var(--accent)}
.mini-list{font-size:13px;line-height:30px}
.mini-list li{list-style:none;display:flex;align-items:center;gap:12px}
.arr{display:inline-block;width:18px;height:12px;background:var(--accent);clip-path:polygon(0 30%,55% 30%,55% 0,100% 50%,55% 100%,55% 70%,0 70%)}
.res-para{font-size:14px;line-height:28px;text-align:right}
/* onsite */
.onsite{top:1970px;height:578px;background:#fff}
.onsite-list li{list-style:none;display:flex;align-items:center;gap:22px;font-weight:700;font-size:15px;height:41px}
/* stats */
.stats{top:2548px;height:308px;background:var(--dark);color:#fff}
.stat{top:105px;width:250px;text-align:center}
.stat b{display:block;font-family:"Poppins",sans-serif;font-weight:600;font-size:38px}
.stat span{display:block;font-size:27px;line-height:40px;margin-top:12px}
/* pricing */
.pricing{top:2856px;height:784px;background:#fff}
.plan{top:184px;width:327px;height:490px;background:#fff;box-shadow:0 4px 16px rgba(0,0,0,.15);overflow:hidden}
.plan h3{position:absolute;left:36px;top:30px;font-family:"Poppins",sans-serif;color:var(--accent);font-weight:600;font-size:24px;line-height:32px;width:260px}
.plan .price{position:absolute;left:36px;top:108px;font-family:"Poppins",sans-serif;font-weight:600;font-size:48px}
.plan p{position:absolute;left:36px;top:196px;width:260px;font-size:13px;line-height:26px}
.plan .btn{position:absolute;left:28px;top:325px;width:200px;height:56px;font-size:17px}
.plan svg{position:absolute;left:0;bottom:0}
/* contact */
.contact{top:3640px;height:622px;background:var(--contact-bg)}
.field{left:635px;width:445px;background:#fff;font-family:"Poppins",sans-serif;font-weight:600;font-size:29px;padding-left:36px;color:#222}
/* logos */
.partners{top:4262px;height:206px;background:#fff}
.partner{top:88px;display:flex;align-items:center;gap:10px;font-family:"Poppins",sans-serif;font-weight:700;font-size:34px;color:#333}
.partner i{width:34px;height:34px;background:#333}
/* newsletter */
.newsletter{top:4468px;height:172px;background:var(--accent)}
/* footer */
.footer{top:4640px;height:380px;background:#fff}
.foot-h{font-family:"Poppins",sans-serif;font-weight:600;font-size:27px}
.foot-links li{list-style:none;font-size:24px;line-height:35px}
.foot-small{font-size:14px;font-weight:600;line-height:22px}
.bottom-bar{top:5020px;height:82px;background:var(--foot-bar)}
</style>
</head>
<body>

<header class="site-header">
  <div class="brand"><div class="brand-dot"></div><div><div class="brand-name">Brimwave.com</div><div class="brand-tag">Tamberlyn Fiber Optics</div></div></div>
  <nav class="nav"><span>Home</span><span>Residential</span><span>Business</span><span>Services</span><span>FAQ</span><span>Telecome</span><span>Contact</span></nav>
  <div class="nav-icons">
    <svg width="20" height="20" viewBox="0 0 20 20"><circle cx="8" cy="8" r="6" fill="none" stroke="#222" stroke-width="2"/><path d="M12.5 12.5 18 18" stroke="#222" stroke-width="2"/></svg>
    <svg width="20" height="22" viewBox="0 0 20 22"><path d="M3 7h14v13H3z" fill="none" stroke="#222" stroke-width="2"/><path d="M6.5 7V5a3.5 3.5 0 0 1 7 0v2" fill="none" stroke="#222" stroke-width="2"/></svg>
  </div>
</header>

<section class="hero">
  <div class="abs hero-kicker">Shine brighter on Tamberlyn</div>
  <h1 class="abs">Tamberlyn Fiber Optic service ,offers low cost, high quality and extremely reliable Phone</h1>
  <p class="abs hero-text">Lorem Ipsum is simply dummy text of the printing and typesetting industry. Lorem Ipsum has been the industry's</p>
  <div class="abs btn btn-accent" style="left:70px;top:398px;width:236px;height:54px">Explore More</div>
  <div class="abs btn btn-outline" style="left:326px;top:398px;width:236px;height:54px">Learn More</div>
  <div class="abs hero-art" role="img" aria-label="Illustration of a connected city of towers with wifi and signal icons"></div>
  <div class="abs dots"><i></i><i></i><i></i></div>
</section>

<section class="services">
  <div class="abs eyebrow" style="left:64px;top:62px">What We Do</div>
  <div class="abs h2" style="left:62px;top:98px">Experience The Difference</div>
  <div class="abs" style="left:64px;top:156px;font-size:19px">Lorem Ipsum is simply dummy text of the printing</div>
  <div class="abs arrows"><i>&larr;</i><i>&rarr;</i></div>

  <div class="abs card" style="left:68px">
    <svg width="58" height="52" viewBox="0 0 58 52"><g fill="none" stroke="#e53935" stroke-width="2.5"><path d="M29 4 54 17 29 30 4 17z"/><path d="M4 26l25 13 25-13"/><path d="M4 35l25 13 25-13"/></g></svg>
    <h3>Local Support</h3><p>Tamberlyn has been the leading choice for high quality and superior .service since 1995</p><a>View Detail &#10148;</a>
  </div>
  <div class="abs card" style="left:340px">
    <svg width="58" height="52" viewBox="0 0 58 52"><g fill="none" stroke="#1fbfa8" stroke-width="2.5"><path d="M14 38c-3-6-3-14 3-20s18-6 24 0 6 14 3 20"/><path d="M20 40c-2-5-2-11 2-15s12-4 16 0 4 10 2 15"/><path d="M26 44c-1-4-1-8 1-10s5-2 5 2-1 8 0 10"/></g></svg>
    <h3>Save Money</h3><p>Tamberlyn has been the leading choice for high quality and superior .service since 1995</p><a>View Detail &#10148;</a>
  </div>
  <div class="abs card" style="left:612px">
    <svg width="58" height="56" viewBox="0 0 58 56"><g fill="none" stroke="#6a4fd8" stroke-width="2.5"><circle cx="29" cy="32" r="20"/><path d="M24 6h10M29 6v6M29 32l8-8"/></g></svg>
    <h3>Getting Started</h3><p>Tamberlyn has been the leading choice for high quality and superior .service since 1995</p><a>View Detail &#10148;</a>
  </div>
  <div class="abs card" style="left:878px">
    <svg width="58" height="56" viewBox="0 0 58 56"><g fill="none" stroke="#f39a1e" stroke-width="2.5"><circle cx="29" cy="28" r="24"/><circle cx="29" cy="24" r="12"/><path d="M20 46l9-10 9 10"/></g></svg>
    <h3>Getting Started</h3><p>Tamberlyn has been the leading choice for high quality and superior .service since 1995</p><a>View Detail &#10148;</a>
  </div>
</section>

<section class="residential">
  <div class="abs photo-circle" style="left:94px;top:58px;width:196px;height:196px;background:linear-gradient(160deg,#d9d2c8,#3d3f4a)" role="img" aria-label="Photo of a businessman talking on a mobile phone"></div>
  <div class="abs res-title" style="left:330px;top:66px;width:540px;text-align:center">Residential <span class="g">Internet Pricing</span><br><span style="margin-right:140px">Plans up to 1 Gigabit</span></div>
  <ul class="abs mini-list" style="left:360px;top:186px">
    <li><span class="arr"></span>High Speed Fiber Optic Internet Connection</li>
    <li style="margin-left:26px"><span class="arr"></span>High Speed Fiber Optic Internet Connection</li>
    <li style="margin-left:44px"><span class="arr"></span>High Speed Fiber Optic Internet Connection</li>
  </ul>
  <svg class="abs" style="left:260px;top:230px" width="690" height="180" viewBox="0 0 690 180"><path d="M10 30 C80 110 240 130 320 100 C420 70 560 100 670 175" fill="none" stroke="var(--accent)" stroke-width="2" stroke-dasharray="8 7"/><circle cx="320" cy="100" r="13" fill="var(--accent)"/></svg>
  <div class="abs res-title" style="left:160px;top:368px;width:600px;text-align:right;line-height:52px">Live in your world. Play in ours<br><span class="g">Save Money</span> &amp; <span class="g">Live Better</span></div>
  <p class="abs res-para" style="left:222px;top:478px;width:540px">By choosing Tamberlyn Internet AND VoIP phone services, you can save money every month by eliminating your per minute long distance rates and extra fees for basic features. Tamberlyn VoIP phone service includes unlimited local and long distance calling within the continental .United States and Canada as well as free Voicemail and Caller ID</p>
  <div class="abs photo-circle" style="left:910px;top:388px;width:196px;height:196px;background:linear-gradient(160deg,#eef4fb,#7fa6cf)" role="img" aria-label="Photo of a smiling woman on a mobile phone"></div>
</section>

<section class="onsite">
  <div class="abs" style="left:66px;top:80px;width:454px;height:412px;background:linear-gradient(135deg,#f1f1ef,#9aa0a8 60%,#2b3342)" role="img" aria-label="Photo of a stressed woman writing at an office desk"></div>
  <div class="abs h2" style="left:578px;top:72px;line-height:54px;font-size:39px">&nbsp;Professional On-Site<br><span class="g">Fiber</span> Installation</div>
  <p class="abs" style="left:574px;top:192px;width:560px;font-size:14px;font-weight:600;line-height:28px">Tamberlyn, Inc. offers service contracts for all of your IT<br>.office needs. We have a new program to buy down your service rate</p>
  <ul class="abs onsite-list" style="left:568px;top:254px">
    <li><span class="arr" style="width:24px;height:16px"></span>Dual Fiber Entrances</li>
    <li><span class="arr" style="width:24px;height:16px"></span>Dual Fiber Entrances</li>
    <li><span class="arr" style="width:24px;height:16px"></span>Dual Fiber Entrances</li>
    <li><span class="arr" style="width:24px;height:16px"></span>Dual Fiber Entrances</li>
  </ul>
  <div class="abs btn btn-accent" style="left:568px;top:440px;width:218px;height:56px;font-weight:600;font-size:16px">Learn More</div>
</section>

<section class="stats">
  <div class="abs stat" style="left:87px"><b>5.2K</b><span>Satisfied Clients</span></div>
  <div class="abs stat" style="left:350px"><b>1.5K</b><span>Domain<br>Registered</span></div>
  <div class="abs stat" style="left:593px"><b>5.2K</b><span>Cup of Coffees</span></div>
  <div class="abs stat" style="left:860px"><b>5.2K</b><span>Error Free Codes</span></div>
</section>

<section class="pricing">
  <div class="abs" style="left:0;width:1226px;top:72px;text-align:center;font-family:'Poppins',sans-serif;font-size:46px;font-weight:400">Our Pricing Plan</div>
  <div class="abs plan" style="left:78px">
    <h3>High Speed Internet Service</h3><div class="price">$55</div>
    <p>Tamberlyn fiber optic service brings the highest quality, fastest, and most reliable internet to your home 25mbps download</p>
    <div class="btn btn-outline">Get The Plan</div>
    <svg width="327" height="90" viewBox="0 0 327 90"><defs><linearGradient id="w1" x1="0" y1="0" x2="0" y2="1"><stop offset="0" stop-color="#5c9cf2"/><stop offset="1" stop-color="#1656b8"/></linearGradient></defs><path d="M0 45 C80 90 140 20 220 45 C270 62 300 40 327 30 V90 H0z" fill="url(#w1)"/></svg>
  </div>
  <div class="abs plan" style="left:444px">
    <h3 style="top:44px">VoIP Phone Service</h3><div class="price">$25</div>
    <p>Tamberlyn fiber optic service brings the highest quality, fastest, and most reliable internet to your home 25mbps download</p>
    <div class="btn btn-outline">Get The Plan</div>
    <svg width="327" height="90" viewBox="0 0 327 90"><path d="M0 45 C80 90 140 20 220 45 C270 62 300 40 327 30 V90 H0z" fill="url(#w1)"/></svg>
  </div>
  <div class="abs plan" style="left:806px">
    <h3>Phone &amp; Internet Packages</h3><div class="price">$80</div>
    <p>Tamberlyn fiber optic service brings the highest quality, fastest, and most reliable internet to your home 25mbps download</p>
    <div class="btn btn-outline">Get The Plan</div>
    <svg width="327" height="90" viewBox="0 0 327 90"><path d="M0 45 C80 90 140 20 220 45 C270 62 300 40 327 30 V90 H0z" fill="url(#w1)"/></svg>
  </div>
</section>

<section class="contact">
  <div class="abs" style="left:90px;top:130px;width:436px;height:380px;background:linear-gradient(160deg,#eef0fb,#c9cdf1 60%,#9aa6e6)" role="img" aria-label="Illustration of a customer support agent with headset at a laptop surrounded by message icons"></div>
  <div class="abs" style="left:580px;top:85px;width:548px;height:470px;background:var(--form-bg)"></div>
  <div class="abs field" style="top:115px;height:65px;line-height:65px">Name</div>
  <div class="abs field" style="top:190px;height:63px;line-height:63px">Email</div>
  <div class="abs field" style="top:260px;height:157px;padding-top:18px">Comments</div>
  <div class="abs btn" style="left:638px;top:438px;width:197px;height:72px;border:2px solid #fff;color:#fff;font-family:'Poppins',sans-serif;font-weight:600;font-size:29px">Send</div>
</section>

<section class="partners">
  <div class="abs partner" style="left:74px"><i></i>NORTHMILL</div>
  <div class="abs partner" style="left:334px;font-size:30px;font-weight:600"><i style="border-radius:50%"></i>BAYLINE</div>
  <div class="abs partner" style="left:602px;font-size:32px"><i></i>quarrytech</div>
  <div class="abs partner" style="left:872px"><i></i>NORTHMILL</div>
</section>

<section class="newsletter">
  <div class="abs" style="left:68px;top:64px;color:#fff;font-family:'Poppins',sans-serif;font-weight:600;font-size:31px">Subscribe to Get Our Newsletter</div>
  <div class="abs" style="left:608px;top:40px;width:540px;height:82px;background:#fff"></div>
  <div class="abs" style="left:648px;top:66px;font-size:23px;font-weight:600">Email Address</div>
  <div class="abs btn" style="left:922px;top:56px;width:211px;height:51px;background:var(--accent);color:#fff;font-family:'Poppins',sans-serif;font-weight:600;font-size:23px">Subscribe</div>
</section>

<footer class="footer">
  <div class="abs" style="left:0;top:0;width:46px;height:60px;border-radius:0 40px 40px 0;background:var(--soft)"></div>
  <div class="abs brand" style="left:70px;top:68px"><div class="brand-dot"></div><div><div class="brand-name">Brimwave.com</div><div class="brand-tag">Tamberlyn Fiber Optics</div></div></div>
  <p class="abs" style="left:78px;top:162px;width:460px;font-size:18px;line-height:31px">Lorem Ipsum is simply dummy text of the printing and typesetting industry. Lorem Ipsum has been the industry's standard dummy text ever since the 1500s,</p>
  <div class="abs" style="left:80px;top:302px;display:flex;gap:18px" aria-label="Social links">
    <i style="width:24px;height:44px;background:#111"></i><i style="width:44px;height:44px;background:#111;border-radius:8px"></i><i style="width:48px;height:40px;background:#111;border-radius:8px;margin-top:3px"></i><i style="width:44px;height:44px;background:#111"></i>
  </div>
  <div class="abs foot-h" style="left:575px;top:30px">Pages</div>
  <ul class="abs foot-links" style="left:576px;top:70px"><li>Home</li><li>Residential</li><li>Business</li><li>Services</li><li>FAQ</li><li>Telecom</li><li>Contact</li></ul>
  <div class="abs foot-h" style="left:862px;top:30px;font-size:25px">Address</div>
  <div class="abs foot-small" style="left:862px;top:70px">Tamberlyn Inc. 48 Larkspur Lane<br>Eastbrook, OR 97301</div>
  <div class="abs foot-h" style="left:862px;top:124px;font-size:25px">Phone</div>
  <div class="abs foot-small" style="left:862px;top:164px">555-014-2290<br>Toll Free: 1-800-555-0199</div>
  <div class="abs foot-h" style="left:862px;top:218px;font-size:25px">Email</div>
  <div class="abs foot-small" style="left:862px;top:258px">Sales: sales@brimwave.com<br>Support: support@brimwave.com</div>
  <svg class="abs" style="left:1040px;top:110px" width="150" height="260" viewBox="0 0 150 260"><circle cx="16" cy="82" r="9" fill="none" stroke="#bcd6f5" stroke-width="2"/><path d="M150 10 110 36 150 58" fill="none" stroke="#bcd6f5" stroke-width="2"/><path d="M50 250 64 220 82 252z" fill="#d6e6fb"/></svg>
</footer>

<div class="abs bottom-bar" style="left:0;width:1200px">
  <div class="abs" style="left:75px;top:32px;font-size:16px;font-weight:600">Brimwave © Copyright 2024 . All Rights Reserved.</div>
  <div class="abs" style="left:1002px;top:30px;display:flex;gap:6px" aria-label="Accepted payment methods">
    <i style="width:28px;height:20px;background:#2c5fb4"></i><i style="width:28px;height:20px;background:#1a3f9a"></i><i style="width:28px;height:20px;background:#e8613a"></i><i style="width:28px;height:20px;background:#3c86d6"></i>
  </div>
</div>

</body>
</html>
```